Boutique Financial Services/Advisor Business Needs Web Design

Looking for an informational and functional web design for my Financial Services/Financial Advisement business. It should have functionality for Company name, address, phone #, "About Us", Who we are, Our Mission, Services we offer, Biographies/Photos of/about "The Team", and possibly a link to "Contact Us". Would like to see something new & exciting blended with a traditional/professional look that will appeal to those approaching retirement, as well as those younger clients that are beginning to think about planning for the future. I already have a web domain through HostMeadow, but would like this to be the design we use for that domain.
Financial Services/Financial Advisor
Coded - Design and coding required
1 page

```html
<!DOCTYPE html>
<html lang="en">
<head>
<meta charset="utf-8">
<title>Summitra Wealth Management</title>
<link href="https://fonts.googleapis.com/css2?family=Playfair+Display:wght@400;500;600&family=Poppins:wght@300;400;500;600&display=swap" rel="stylesheet">
<style>
:root{
  --navy:#13124a;
  --navy-deep:#0e0d3a;
  --grey:#8a8a8a;
  --grey-band:#7d7d7f;
  --ink:#222233;
  --muted:#6b6b78;
  --white:#ffffff;
  --gold:#f2b531;
  --photo-warm:linear-gradient(135deg,#c9b9a6,#8f7f74 55%,#5a5566);
  --photo-cool:linear-gradient(135deg,#dfe3ea,#a9b2c2 50%,#5d6478);
}
*{box-sizing:border-box;margin:0;padding:0}
html,body{width:1200px;height:3772px;overflow:hidden}
body{position:relative;font-family:'Poppins',sans-serif;color:var(--ink);background:var(--white)}
.serif{font-family:'Playfair Display',serif}
section,header,footer{position:absolute;left:0;width:1200px}
.photo{position:absolute}
.btn{display:inline-block;font-size:11px;font-weight:500;padding:10px 26px;border-radius:2px}
p{font-size:12px;line-height:1.7}

/* header */
.site-header{top:0;height:100px;display:flex;align-items:center;padding:0 140px}
.brand{font-family:'Playfair Display',serif;font-size:15px;font-weight:600;color:var(--navy);letter-spacing:1px;line-height:1.25;width:170px}
.main-nav{display:flex;gap:26px;margin-left:70px;font-size:12px;color:var(--ink)}
.contact-mini{display:flex;gap:28px;margin-left:auto}
.mini{display:flex;align-items:center;gap:8px}
.mini .ic{width:30px;height:30px;border-radius:50%;background:var(--navy);display:flex;align-items:center;justify-content:center}
.mini small{display:block;font-size:9px;color:var(--muted)}
.mini b{font-size:13px;color:var(--navy);font-weight:600}

/* hero */
.hero{top:100px;height:520px;background:var(--navy)}
.hero-text{position:absolute;left:140px;top:80px;width:390px;color:var(--white)}
.hero-text h1{font-size:44px;font-weight:500;line-height:1.15;margin-bottom:18px}
.hero-text p{color:#cfd0e6}
.hero-text .btn{background:var(--white);color:var(--navy);margin-top:26px}
.rating{margin-top:26px;font-size:11px;color:#cfd0e6}
.rating span{color:var(--gold);font-size:16px;letter-spacing:2px;margin-right:6px}
.hero .photo{left:570px;top:0;width:630px;height:520px;background:var(--photo-cool)}

/* empowering */
.empower{top:620px;height:600px}
.empower .photo.main{left:0;top:40px;width:470px;height:540px;background:var(--photo-warm)}
.empower .photo.inset{left:300px;top:180px;width:230px;height:210px;background:var(--photo-cool);border:8px solid var(--white)}
.empower-text{position:absolute;left:600px;top:50px;width:430px}
.frame-title{border-left:2px solid var(--navy);border-top:2px solid var(--navy);padding:18px 0 0 18px;margin-bottom:20px}
.frame-title h2{font-size:34px;font-weight:500;color:var(--navy);line-height:1.2}
.empower-text p{color:var(--muted);margin-bottom:16px}
.empower-text .btn{background:var(--navy);color:var(--white);margin-top:6px}

/* purpose */
.purpose{top:1220px;height:480px}
.purpose .band{position:absolute;top:0;left:0;width:1200px;height:400px;background:var(--navy)}
.purpose-head{position:absolute;top:80px;width:1200px;text-align:center;color:var(--white)}
.purpose-head h2{font-size:38px;font-weight:500;margin-bottom:14px}
.purpose-head p{width:520px;margin:0 auto;color:#cfd0e6}
.cards3{position:absolute;top:240px;left:190px;display:flex;gap:20px}
.value-card{width:260px;height:150px;background:var(--white);text-align:center;padding:34px 20px 0;box-shadow:0 6px 18px rgba(0,0,0,.12);position:relative}
.value-card.alt{background:var(--grey);color:var(--white)}
.value-card .badge{position:absolute;left:50%;top:-18px;transform:translateX(-50%);width:36px;height:36px;border-radius:50%;background:var(--navy);border:3px solid var(--white)}
.value-card h3{font-family:'Playfair Display',serif;font-size:20px;font-weight:500;color:var(--navy);margin-bottom:8px}
.value-card.alt h3{color:var(--white)}
.value-card p{font-size:10px;line-height:1.6;color:var(--muted)}
.value-card.alt p{color:#eee}

/* experts */
.experts{top:1700px;height:600px}
.experts-text{position:absolute;left:140px;top:70px;width:400px}
.experts-text h2{font-size:38px;font-weight:500;color:var(--navy);line-height:1.2;margin-bottom:16px}
.experts-text > p{color:var(--muted);margin-bottom:26px}
.step{display:flex;gap:18px;align-items:center;margin-bottom:22px}
.step .num{flex:none;width:42px;height:42px;border-radius:50%;background:var(--navy);color:var(--white);font-size:12px;display:flex;align-items:center;justify-content:center}
.step p{font-size:11px;color:var(--muted)}
.experts .btn{background:#555;color:var(--white)}
.experts .photo{left:640px;top:80px;width:370px;height:440px;background:var(--photo-warm)}

/* services */
.services{top:2300px;height:740px;background:var(--navy)}
.services-head{position:absolute;top:80px;width:1200px;text-align:center;color:var(--white)}
.services-head h2{font-size:38px;font-weight:500;line-height:1.2;margin-bottom:14px}
.services-head p{width:520px;margin:0 auto;color:#cfd0e6}
.service-row{position:absolute;top:275px;left:180px;display:flex;gap:26px}
.service-card{width:262px;background:var(--white);position:relative}
.service-card .photo{position:relative;height:170px}
.service-card .ic{position:absolute;left:20px;top:150px;width:40px;height:40px;border-radius:50%;background:var(--navy);border:3px solid var(--white)}
.service-card .body{padding:30px 20px 22px}
.service-card h3{font-family:'Playfair Display',serif;font-size:13px;font-weight:500;color:var(--navy);letter-spacing:.5px;margin-bottom:6px;text-transform:uppercase}
.service-card p{font-size:10px;line-height:1.6;color:var(--muted)}
.slider-nav{position:absolute;top:660px;left:400px;width:400px;display:flex;align-items:center;gap:14px}
.slider-nav .line{flex:1;height:1px;background:#5a5a88}

/* contact */
.contact{top:3040px;height:260px;background:var(--grey-band)}
.contact-left{position:absolute;left:140px;top:50px;color:var(--white)}
.contact-left h2{font-size:36px;font-weight:500;line-height:1.15;margin-bottom:18px}
.contact-left .mini b,.contact-left .mini small{color:var(--white)}
.contact-left .row{display:flex;gap:30px}
.contact-left .btn{background:var(--white);color:var(--ink);margin-top:18px}
.contact-left .mini .ic{background:var(--navy)}
.contact-links{position:absolute;left:620px;top:60px;display:flex;gap:120px;font-size:11px;color:var(--white)}
.contact-links ul{list-style:none}
.contact-links li{margin-bottom:18px;padding-bottom:6px;border-bottom:1px solid #9a9a9c;width:150px}

/* footer */
.site-footer{top:3300px;height:472px;text-align:center}
.footer-brand{font-family:'Playfair Display',serif;font-size:26px;font-weight:600;color:var(--navy);letter-spacing:2px;line-height:1.25;margin-top:70px}
.site-footer > p{width:460px;margin:18px auto 0;color:var(--muted);font-size:11px}
.footer-nav{position:absolute;top:250px;left:180px;width:840px;height:38px;background:var(--navy);display:flex;justify-content:space-around;align-items:center;font-size:11px;color:var(--white)}
.socials{position:absolute;top:320px;width:1200px;display:flex;justify-content:center;gap:12px}
.socials span{width:26px;height:26px;border-radius:50%;background:var(--navy)}
.copyright{position:absolute;top:420px;width:1200px;font-size:10px;color:var(--muted)}
.copyright b{color:var(--navy)}
</style>
</head>
<body>

<header class="site-header">
  <div class="brand">SUMMITRA<br>WEALTH</div>
  <nav class="main-nav">
    <span>Home</span><span>About Us</span><span>Who we are</span><span>Our Mission</span><span>Services</span><span>The Team</span>
  </nav>
  <div class="contact-mini">
    <div class="mini">
      <span class="ic"><svg width="14" height="14" viewBox="0 0 24 24"><path fill="#fff" d="M6.6 10.8a15 15 0 006.6 6.6l2.2-2.2c.3-.3.7-.4 1-.2 1.1.4 2.3.6 3.6.6.6 0 1 .4 1 1V20c0 .6-.4 1-1 1A17 17 0 013 4c0-.6.4-1 1-1h3.5c.6 0 1 .4 1 1 0 1.3.2 2.5.6 3.6.1.3 0 .7-.2 1z"/></svg></span>
      <div><small>Call Now</small><b>555-014-2290</b></div>
    </div>
    <div class="mini">
      <span class="ic"><svg width="14" height="14" viewBox="0 0 24 24"><path fill="#fff" d="M3 5h18v14H3z"/><path fill="none" stroke="#13124a" stroke-width="2" d="M3 6l9 7 9-7"/></svg></span>
      <div><small>Email Us</small><b>Lorem ipsum</b></div>
    </div>
  </div>
</header>

<section class="hero">
  <div class="hero-text">
    <h1 class="serif">Guiding You Through Every Financial Milestone</h1>
    <p>Lorem ipsum is simply dummy text of the printing and typesetting industry. Lorem ipsum has been the industry's standard dummy text ever since the 1500s.</p>
    <span class="btn">Contact Us</span>
    <div class="rating"><span>★★★★★</span>From 120 Reviews</div>
  </div>
  <div class="photo" role="img" aria-label="Two advisors smiling while reviewing documents at a laptop"></div>
</section>

<section class="empower">
  <div class="photo main" role="img" aria-label="Advisors meeting with clients around a table"></div>
  <div class="photo inset" role="img" aria-label="Business people shaking hands across a desk"></div>
  <div class="empower-text">
    <div class="frame-title"><h2 class="serif">Empowering You To Achieve Your Financial Goals</h2></div>
    <p>Lorem ipsum is simply dummy text of the printing and typesetting industry. Lorem ipsum has been the industry's standard dummy text ever since the 1500s, when an unknown printer took a galley of type and scrambled it to make a type specimen book.</p>
    <p>It has survived not only five centuries but also the leap into electronic typesetting, remaining essentially unchanged. It was popularised in the 1960s with the release of sheets containing Lorem Ipsum passages, and more recently with desktop publishing software.</p>
    <span class="btn">Contact Us</span>
  </div>
</section>

<section class="purpose">
  <div class="band"></div>
  <div class="purpose-head">
    <h2 class="serif">Your Success, Our Purpose</h2>
    <p>Lorem ipsum is simply dummy text of the printing and typesetting industry. Lorem ipsum has been the industry's standard dummy text ever since the 1500s.</p>
  </div>
  <div class="cards3">
    <div class="value-card"><span class="badge"></span><h3>Building Trust</h3><p>Building lasting relationships with honest and clear guidance.</p></div>
    <div class="value-card alt"><span class="badge"></span><h3>Delivering Results</h3><p>Focused planning that helps your wealth grow over time.</p></div>
    <div class="value-card"><span class="badge"></span><h3>Educating Clients</h3><p>Helping you make informed decisions with confidence.</p></div>
  </div>
</section>

<section class="experts">
  <div class="experts-text">
    <h2 class="serif">Experts In<br>Financial Guidance</h2>
    <p>Lorem ipsum is simply dummy text of the printing and typesetting industry.</p>
    <div class="step"><span class="num">01</span><p>Lorem ipsum is simply dummy text of the printing and typesetting industry. Lorem ipsum has been.</p></div>
    <div class="step"><span class="num">02</span><p>Lorem ipsum is simply dummy text of the printing and typesetting industry standard dummy text.</p></div>
    <div class="step"><span class="num">03</span><p>Lorem ipsum is simply dummy text of the printing and typesetting industry.</p></div>
    <span class="btn">Learn More</span>
  </div>
  <div class="photo" role="img" aria-label="Team of advisors gathered around a laptop in an office"></div>
</section>

<section class="services">
  <div class="services-head">
    <h2 class="serif">Our Financial Services<br>Tailored To Your Needs</h2>
    <p>Lorem ipsum is simply dummy text of the printing and typesetting industry. Lorem ipsum has been the industry's standard dummy text ever since the 1500s.</p>
  </div>
  <div class="service-row">
    <div class="service-card">
      <div class="photo" style="background:var(--photo-warm)" role="img" aria-label="Retired couple meeting with an advisor"></div>
      <span class="ic"></span>
      <div class="body"><h3>Retirement Planning</h3><p>Lorem ipsum is simply dummy text of the printing and typesetting.</p></div>
    </div>
    <div class="service-card">
      <div class="photo" style="background:var(--photo-cool)" role="img" aria-label="Advisors discussing investment charts"></div>
      <span class="ic"></span>
      <div class="body"><h3>Investment Management</h3><p>Lorem ipsum is simply dummy text of the printing and typesetting.</p></div>
    </div>
    <div class="service-card">
      <div class="photo" style="background:var(--photo-warm)" role="img" aria-label="Young family reviewing plans with an advisor"></div>
      <span class="ic"></span>
      <div class="body"><h3>Wealth Management</h3><p>Lorem ipsum is simply dummy text of the printing and typesetting.</p></div>
    </div>
  </div>
  <div class="slider-nav">
    <svg width="14" height="14" viewBox="0 0 24 24"><path fill="none" stroke="#fff" stroke-width="3" d="M15 4l-8 8 8 8"/></svg>
    <span class="line"></span>
    <svg width="14" height="14" viewBox="0 0 24 24"><path fill="none" stroke="#fff" stroke-width="3" d="M9 4l8 8-8 8"/></svg>
  </div>
</section>

<section class="contact">
  <div class="contact-left">
    <h2 class="serif">Get In Touch<br>With Us Today</h2>
    <div class="row">
      <div class="mini">
        <span class="ic"><svg width="14" height="14" viewBox="0 0 24 24"><path fill="#fff" d="M6.6 10.8a15 15 0 006.6 6.6l2.2-2.2c.3-.3.7-.4 1-.2 1.1.4 2.3.6 3.6.6.6 0 1 .4 1 1V20c0 .6-.4 1-1 1A17 17 0 013 4c0-.6.4-1 1-1h3.5c.6 0 1 .4 1 1 0 1.3.2 2.5.6 3.6.1.3 0 .7-.2 1z"/></svg></span>
        <div><small>Call Now</small><b>555-014-2290</b></div>
      </div>
      <div class="mini">
        <span class="ic"><svg width="14" height="14" viewBox="0 0 24 24"><path fill="#fff" d="M3 5h18v14H3z"/><path fill="none" stroke="#13124a" stroke-width="2" d="M3 6l9 7 9-7"/></svg></span>
        <div><small>Email Us</small><b>Lorem ipsum</b></div>
      </div>
    </div>
    <span class="btn">Submit</span>
  </div>
  <div class="contact-links">
    <ul><li>First Name</li><li>Email</li><li>Message</li></ul>
    <ul><li>Last Name</li><li>Phone Number</li></ul>
  </div>
</section>

<footer class="site-footer">
  <div class="footer-brand">SUMMITRA<br>WEALTH MANAGEMENT</div>
  <p>Lorem ipsum dolor sit amet, consectetur adipiscing elit, sed do eiusmod tempor incididunt ut labore et dolore magna aliqua.</p>
  <nav class="footer-nav">
    <span>Home</span><span>About Us</span><span>Who we are</span><span>Our Mission</span><span>Services</span><span>The Team</span><span>Contact Us</span>
  </nav>
  <div class="socials"><span></span><span></span><span></span><span></span><span></span></div>
  <div class="copyright">Copyright © 2024 <b>SUMMITRA WEALTH MANAGEMENT</b> | Privacy Policy | Terms &amp; Conditions</div>
</footer>

</body>
</html>
```